KLT Website Homepage Redesign

My website needs a homepage redesign and banner photos updates for Discovery and SEO Services pages. We sell Search Engine Optimization services. We use Search Engine Optimization techniques to help our clients rank high in search engines like Zorvix. It is an intense competition to consistently rank above other businesses. The problem is there is no easy way to show what the benefits of Search Engine Optimization services look like in an emotional way. I want to use an image from sailboat racing to dramatize that our clients win at Search Engine Optimization marketing.
The following products are desired:
1. Desktop version homepage redesign with a banner that clearly shows we sell Search Engine Optimization services using sailboat racing as a metaphor.
2. Mobile version homepage redesign with a banner that clearly shows we sell Search Engine Optimization services using sailboat racing as a metaphor.
2. New banner photo for the Discovery Page
3. New banner photo for the SEO page
The design must be responsive and show well on desktops, laptops, tablets and mobile phones. The current footer style must be kept. A third service called SEO must be added.
the website URL is www.velmorbix.com
Target Market(s)
Business to Business
Industry/Entity Type
Digital Marketing
Coding
Coded - Design and coding required
Number of Pages Required
1 page
Colors
Designer to choose colors to be used in the design.
Look and feel
Each slider illustrates characteristics of the customer's brand and the style your logo design should communicate.

```html
<!DOCTYPE html>
<html lang="en">
<head>
<meta charset="utf-8">
<meta name="viewport" content="width=device-width, initial-scale=1">
<title>KLT — SEO Services Homepage</title>
<link href="https://fonts.googleapis.com/css2?family=Poppins:wght@400;500;600;700&family=Roboto:wght@400;500&display=swap" rel="stylesheet">
<style>
:root{
  --bg:#f4f5f8;
  --page:#f9f9fb;
  --blue-a:#4a63b3;
  --blue-b:#31a2d5;
  --purple:#5449a1;
  --teal:#1fc3cb;
  --ink:#2a2d3a;
  --muted:#6b7080;
  --white:#ffffff;
  --dark:#1f2024;
  --orange:#f5a623;
  --sea:#1f6fae;
  --sail:#e8f3fb;
}
*{box-sizing:border-box;margin:0;padding:0}
html,body{width:1200px;height:2195px;overflow:hidden;background:var(--bg)}
body{font-family:"Roboto",sans-serif;color:var(--ink);position:relative}
.page{position:absolute;left:282px;top:111px;width:633px;height:1973px;background:var(--page);overflow:hidden;box-shadow:0 10px 40px rgba(60,80,140,.08)}
.abs{position:absolute}
h1,h2,h3,h4,.head{font-family:"Poppins",sans-serif}
.btn{position:absolute;display:flex;align-items:center;justify-content:center;font-family:"Poppins",sans-serif;font-weight:600;font-size:5.5px;border-radius:2px}

/* hero */
.hero{position:absolute;left:0;top:0;width:633px;height:300px}
.logo-box{left:127px;top:0;width:62px;height:36px;background:var(--white);display:flex;align-items:center;justify-content:center;font-family:"Poppins",sans-serif;font-weight:500;font-size:14px;color:var(--blue-a)}
.nav{left:323px;top:13px;display:flex;gap:7px;align-items:center;font-size:4.4px;color:var(--white)}
.nav .login{background:#5a63c4;border-radius:6px;padding:3px 11px}
.hero-title{left:134px;top:87px;font-size:15px;line-height:1.3;font-weight:700;color:var(--white)}
.hero-text{left:134px;top:135px;width:160px;font-size:5.3px;line-height:1.6;color:#e4ecfa}
.hero .btn{left:134px;top:169px;width:66px;height:19px;background:var(--white);color:var(--blue-a)}
.hero-art{left:357px;top:44px;width:180px;height:176px;border-radius:14px;background:linear-gradient(180deg,#8fd6ef 0%,#bfe7f6 48%,#2f8fcf 52%,#1d5fa0 100%);opacity:.85}
.play{left:299px;top:265px;width:28px;height:28px;border-radius:50%;background:var(--white);border:3px solid #b6c6ea;display:flex;align-items:center;justify-content:center}
.play-label{left:290px;top:300px;width:46px;text-align:center;font-size:4.6px;color:var(--blue-a);font-weight:500}

/* intro */
.sec-title{left:0;width:633px;text-align:center;font-size:11px;font-weight:500;line-height:1.4;color:var(--ink)}
.sec-text{left:186px;width:262px;text-align:center;font-size:5.2px;line-height:1.6;color:var(--muted)}
.rule{height:1px;width:40px;left:296px;background:#9aa6c8}
.cards{left:134px;top:422px;width:366px;height:113px;display:flex}
.card{width:91.5px;height:113px;position:relative;background:linear-gradient(180deg,#5d6fc4,#3b8fcf);overflow:hidden}
.card .top{position:absolute;left:0;top:0;width:100%;height:52px;background:var(--white)}
.card svg.wave{position:absolute;left:0;top:38px}
.card .ico{position:absolute;left:34px;top:14px;width:22px;height:22px}
.card h4{position:absolute;top:63px;width:100%;text-align:center;font-size:5.6px;font-weight:600;color:var(--white)}
.card p{position:absolute;top:75px;left:6px;right:6px;text-align:center;font-size:4px;line-height:1.45;color:#e6ecfb}
.card.active{border-top:2px solid var(--blue-a)}
.teal{background:var(--teal);color:var(--white)}

/* tools */
.laptop{left:89px;top:604px;width:240px;height:168px;border-radius:8px;background:linear-gradient(180deg,#dfe4ef,#b9c0cf)}
.tools-title{left:357px;top:618px;font-size:11px;font-weight:500;line-height:1.4}
.tools-text{left:357px;top:660px;width:140px;font-size:5.2px;line-height:1.6;color:var(--muted)}
.ticks{left:357px;top:684px;list-style:none;font-size:4.6px;color:#40465a}
.ticks li{display:flex;gap:4px;align-items:center;margin-bottom:3.5px}

/* services */
.services{left:0;top:825px;width:633px;height:331px;background:linear-gradient(135deg,var(--purple) 0%,#3f7cc2 55%,#23c1d6 100%)}
.services .sec-title,.services .sec-text{color:var(--white)}
.diamond{position:absolute;width:58px;height:58px;border:1px solid rgba(255,255,255,.55);transform:rotate(45deg)}
.diamond.big{background:var(--white);border:none;width:70px;height:70px;box-shadow:0 8px 20px rgba(0,0,0,.15)}
.svc-ico{position:absolute;width:20px;height:20px;border-radius:5px;background:rgba(255,255,255,.85)}
.svc-title{left:342px;top:166px;font-size:7.5px;font-weight:600;color:var(--white);line-height:1.5}
.svc-text{left:342px;top:196px;width:158px;font-size:4.8px;line-height:1.65;color:#e7eefa}

/* pricing */
.price{position:absolute;top:1259px;width:115px;height:166px;border-radius:2px;color:var(--white);text-align:center;font-family:"Poppins",sans-serif}
.price .name{margin-top:16px;font-size:7px;font-weight:500}
.price .amt{margin-top:6px;font-size:18px;font-style:italic;font-weight:500}
.price .term{margin-top:2px;font-size:11px;font-weight:600}
.price p{margin:10px 10px 0;font-family:"Roboto",sans-serif;font-size:4.6px;line-height:1.6;opacity:.9}
.price hr{border:none;height:1px;width:48px;margin:10px auto 0;background:rgba(255,255,255,.45)}
.price .btn{position:relative;margin:10px auto 0;width:66px;height:18px;color:var(--white)}
.basic{left:134px;background:linear-gradient(180deg,#7a3f9a,#ea1f6b)}
.standard{left:258px;background:linear-gradient(180deg,#6fd6c2,#2dbde0)}
.pro{left:383px;background:linear-gradient(180deg,#25b7e0,#4468bd)}

/* testimonial */
.t-title{left:134px;top:1488px;font-size:11px;font-weight:500;line-height:1.4}
.t-text{left:134px;top:1530px;width:180px;font-size:5px;line-height:1.6;color:var(--muted)}
.t-figure{left:134px;top:1559px;width:52px;height:134px;border-radius:26px 26px 6px 6px;background:linear-gradient(180deg,#6d6a80,#3a3d52)}
.quote{left:185px;top:1563px;width:167px;height:86px;background:var(--white);box-shadow:0 6px 20px rgba(60,80,140,.1);overflow:hidden}
.quote .mark{position:absolute;left:11px;top:3px;font-size:16px;color:#c8ccd8;font-family:"Poppins",sans-serif}
.quote p{position:absolute;left:11px;top:22px;width:140px;font-size:4.6px;line-height:1.6;color:#444a5c}
.quote .who{position:absolute;left:11px;top:64px;display:flex;gap:5px;align-items:center}
.quote .who b{display:block;font-size:5.3px;font-weight:500;color:var(--ink)}
.quote .who span{font-size:3.8px;color:var(--muted)}
.avatar{border-radius:50%;background:linear-gradient(135deg,#c9a48f,#7b5b4f)}
.orbit{position:absolute;border-radius:50%;border:1px solid #e3e6ee}

/* partners */
.partners{left:134px;top:1748px;width:366px;display:flex;justify-content:space-between;font-family:"Poppins",sans-serif;font-size:11px;font-weight:500;color:#b7bac4}

/* footer */
.footer{left:0;top:1800px;width:633px;height:173px;background:var(--dark);color:#d8d9de}
.footer .brand{left:134px;top:14px;font-family:"Poppins",sans-serif;font-size:14px;font-weight:500;color:var(--white)}
.fcol{position:absolute;top:30px;font-size:4.6px;line-height:2.45}
.fcol h5{font-family:"Poppins",sans-serif;font-size:5.6px;font-weight:500;color:var(--white);padding-bottom:4px;margin-bottom:4px;border-bottom:1px solid #44464d;width:24px;white-space:nowrap}
.social{display:flex;gap:4px;margin-top:4px}
.social i{width:9px;height:9px;border-radius:50%;border:1px solid #c8c9cf;display:block}
.social i.pink{background:#e8407a;border-color:#e8407a}
.news{left:410px;top:30px;width:90px}
.news-input{margin-top:8px;width:86px;height:14px;border-radius:7px;background:#2d2f35;position:relative}
.news-input i{position:absolute;right:0;top:0;width:14px;height:14px;border-radius:50%;background:#2a8ee0}
.bottom{position:absolute;left:134px;right:133px;top:160px;display:flex;justify-content:space-between;font-size:4.2px;color:#b3b5bc}
.bottom nav{display:flex;gap:6px}

/* responsive: tablet and phone scale the layout to the viewport width */
@media (max-width:1199px){
  html,body{width:100%;height:auto;overflow-x:hidden}
  .page{left:0;top:0;transform-origin:top left;box-shadow:none}
}
@media (max-width:1199px) and (min-width:900px){.page{transform:scale(1.42)}}
@media (max-width:899px) and (min-width:640px){.page{transform:scale(1.01)}}
@media (max-width:639px) and (min-width:400px){.page{transform:scale(.63)}}
@media (max-width:399px){.page{transform:scale(.59)}}
</style>
</head>
<body>
<main class="page">

  <!-- hero -->
  <section class="hero">
    <svg class="abs" width="633" height="300" viewBox="0 0 633 300" style="left:0;top:0">
      <defs>
        <linearGradient id="heroGrad" x1="0" y1="0" x2="1" y2="1">
          <stop offset="0" stop-color="#4a63b3"/><stop offset="1" stop-color="#2fa5d5"/>
        </linearGradient>
        <linearGradient id="waveGrad" x1="0" x2="1">
          <stop offset="0" stop-color="#2f92cd"/><stop offset="1" stop-color="#62d3e3"/>
        </linearGradient>
      </defs>
      <path d="M0 0H633V284C590 250 520 220 440 232C370 242 340 268 300 278C230 296 180 230 120 238C70 244 30 266 0 284Z" fill="url(#heroGrad)"/>
      <path d="M0 284C40 250 90 236 140 238C200 240 240 272 300 276C360 280 400 238 460 236C530 234 590 258 633 284V300H0Z" fill="url(#waveGrad)" opacity=".6"/>
      <path d="M0 290C50 262 110 258 170 266C230 274 270 290 320 286C380 282 420 262 480 262C550 262 600 278 633 294V300H0Z" fill="#f9f9fb"/>
      <g fill="#e0647a"><circle cx="35" cy="156" r="1.5"/><circle cx="310" cy="66" r="1.5"/><circle cx="586" cy="38" r="1.5"/><circle cx="64" cy="210" r="1.5"/></g>
      <g fill="#4dd6a0"><circle cx="495" cy="62" r="1.5"/><circle cx="565" cy="168" r="1.5"/><circle cx="313" cy="228" r="1.5"/><circle cx="35" cy="256" r="1.5"/></g>
    </svg>
    <div class="abs logo-box">KLT</div>
    <nav class="abs nav"><span>About</span><span>Services</span><span>Pricing</span><span>Testimonial</span><span>Blog</span><span>Contact</span><span class="login">Login</span></nav>
    <h1 class="abs hero-title">Win The Search Race<br>With Expert SEO</h1>
    <p class="abs hero-text">We steer your business ahead of the fleet and into the top results on Zorvix.</p>
    <a class="btn">Free Analysis</a>
    <div class="abs hero-art" role="img" aria-label="Illustration of racing sailboats crossing the finish line ahead of the fleet"></div>
    <div class="abs play"><svg width="8" height="8" viewBox="0 0 8 8"><path d="M2 1L7 4L2 7Z" fill="#4a63b3"/></svg></div>
    <div class="abs play-label">Play Video</div>
  </section>

  <!-- intro -->
  <h2 class="abs sec-title" style="top:342px">Market Mind Boost Your<br>Web Traffic</h2>
  <p class="abs sec-text" style="top:377px">Lorem ipsum dolor sit amet, consectetur adipiscing elit, sed do eiusmod tempor incididunt ut labore et dolore magna aliqua.</p>
  <div class="abs rule" style="top:399px"></div>

  <div class="abs cards">
    <article class="card"><div class="top"></div>
      <svg class="wave" width="92" height="20" viewBox="0 0 92 20"><path d="M0 14C20 0 40 0 46 8C56 20 76 10 92 2V20H0Z" fill="#8aa0dc"/></svg>
      <svg class="ico" viewBox="0 0 22 22"><path d="M3 15L10 9L14 12L19 5" fill="none" stroke="#2e8fd0" stroke-width="1.5"/><circle cx="17" cy="5" r="2" fill="#1fc3cb"/></svg>
      <h4>Speed Optimization</h4><p>Lorem ipsum dolor sit amet, consectetur adipiscing elit, sed do eiusmod tempor incididunt ut labore et dolore magna aliqua.</p></article>
    <article class="card active"><div class="top"></div>
      <svg class="wave" width="92" height="20" viewBox="0 0 92 20"><path d="M0 14C20 0 40 0 46 8C56 20 76 10 92 2V20H0Z" fill="#8aa0dc"/></svg>
      <svg class="ico" viewBox="0 0 22 22"><circle cx="10" cy="9" r="6" fill="none" stroke="#2d3a6a" stroke-width="1.6"/><path d="M14 13L19 18" stroke="#2d3a6a" stroke-width="2"/><path d="M8 11V9M10 11V6M12 11V8" stroke="#2e8fd0" stroke-width="1.2"/></svg>
      <h4>Marketing Goal</h4><p>Lorem ipsum dolor sit amet, consectetur adipiscing elit, sed do eiusmod tempor incididunt ut labore et dolore magna aliqua.</p></article>
    <article class="card"><div class="top"></div>
      <svg class="wave" width="92" height="20" viewBox="0 0 92 20"><path d="M0 14C20 0 40 0 46 8C56 20 76 10 92 2V20H0Z" fill="#8aa0dc"/></svg>
      <svg class="ico" viewBox="0 0 22 22"><circle cx="10" cy="9" r="6" fill="none" stroke="#2d3a6a" stroke-width="1.6"/><path d="M14 13L19 18" stroke="#2d3a6a" stroke-width="2"/><path d="M6 11L9 8L11 10L14 6" fill="none" stroke="#1fc3cb" stroke-width="1.2"/></svg>
      <h4>Analysis</h4><p>Lorem ipsum dolor sit amet, consectetur adipiscing elit, sed do eiusmod tempor incididunt ut labore et dolore magna aliqua.</p></article>
    <article class="card"><div class="top"></div>
      <svg class="wave" width="92" height="20" viewBox="0 0 92 20"><path d="M0 14C20 0 40 0 46 8C56 20 76 10 92 2V20H0Z" fill="#8aa0dc"/></svg>
      <svg class="ico" viewBox="0 0 22 22"><rect x="4" y="10" width="14" height="8" fill="none" stroke="#2d3a6a" stroke-width="1.4"/><circle cx="11" cy="6" r="3" fill="#f5c04a"/><path d="M4 13H18" stroke="#2e8fd0"/></svg>
      <h4>Customer Experience</h4><p>Lorem ipsum dolor sit amet, consectetur adipiscing elit, sed do eiusmod tempor incididunt ut labore et dolore magna aliqua.</p></article>
  </div>
  <a class="btn teal" style="left:283px;top:552px;width:66px;height:19px">Learn More</a>

  <!-- tools -->
  <div class="abs laptop" role="img" aria-label="Laptop showing an SEO analytics dashboard"></div>
  <h2 class="abs tools-title">Live Marketing Analysis<br>Web Tools</h2>
  <p class="abs tools-text">Lorem ipsum dolor sit amet, consectetur adipiscing elit, sed do eiusmod tempor incididunt</p>
  <ul class="abs ticks">
    <li><svg width="5" height="5" viewBox="0 0 5 5"><rect x=".3" y=".3" width="4.4" height="4.4" fill="none" stroke="#2e8fd0" stroke-width=".6"/><path d="M1 2.5L2 3.5L4 1.3" fill="none" stroke="#2e8fd0" stroke-width=".6"/></svg>Lorem ipsum dolor sit amet, consectetur adipisc-</li>
    <li><svg width="5" height="5" viewBox="0 0 5 5"><rect x=".3" y=".3" width="4.4" height="4.4" fill="none" stroke="#2e8fd0" stroke-width=".6"/><path d="M1 2.5L2 3.5L4 1.3" fill="none" stroke="#2e8fd0" stroke-width=".6"/></svg>Lorem ipsum dolor sit amet, consectetur</li>
    <li><svg width="5" height="5" viewBox="0 0 5 5"><rect x=".3" y=".3" width="4.4" height="4.4" fill="none" stroke="#2e8fd0" stroke-width=".6"/><path d="M1 2.5L2 3.5L4 1.3" fill="none" stroke="#2e8fd0" stroke-width=".6"/></svg>Lorem ipsum dolor sit amet, consectetur adipiscing</li>
  </ul>
  <a class="btn teal" style="left:357px;top:723px;width:66px;height:19px">14 Days Trial</a>

  <!-- services -->
  <section class="abs services">
    <h2 class="abs sec-title" style="top:40px">We Are Provide In The<br>Following Services</h2>
    <p class="abs sec-text" style="top:75px">Lorem ipsum dolor sit amet, consectetur adipiscing elit, sed do eiusmod tempor incididunt ut labore et dolore magna aliqua.</p>
    <div class="diamond" style="left:196px;top:131px"></div>
    <div class="diamond" style="left:148px;top:179px"></div>
    <div class="diamond" style="left:196px;top:227px"></div>
    <div class="diamond big" style="left:238px;top:174px"></div>
    <div class="svc-ico" style="left:215px;top:150px" role="img" aria-label="Email marketing icon"></div>
    <div class="svc-ico" style="left:167px;top:198px" role="img" aria-label="Team monitor icon"></div>
    <div class="svc-ico" style="left:215px;top:246px" role="img" aria-label="Search analysis icon"></div>
    <svg class="abs" style="left:261px;top:196px" width="26" height="24" viewBox="0 0 26 24">
      <rect x="2" y="10" width="5" height="12" fill="none" stroke="#4a63b3" stroke-width="1.4"/>
      <rect x="10" y="3" width="5" height="19" fill="#1fc3cb"/>
      <rect x="18" y="13" width="5" height="9" fill="none" stroke="#4a63b3" stroke-width="1.4"/>
      <path d="M0 23H26" stroke="#4a63b3" stroke-width="1.4"/>
    </svg>
    <h3 class="abs svc-title">Keyword Research &amp;<br>Marketing</h3>
    <p class="abs svc-text">Lorem ipsum dolor sit amet, consectetur adipiscing elit, sed do eiusmod tempor incididunt ut labore et dolore magna aliqua. Quis ipsum suspendisse ultrices gravida. Risus commodo viverra maecenas accumsan lacus vel facilisis.</p>
  </section>

  <!-- pricing -->
  <h2 class="abs sec-title" style="top:1184px">No Extra Charges! Choose Your<br>Plan Now</h2>
  <p class="abs sec-text" style="top:1219px">Lorem ipsum dolor sit amet, consectetur adipiscing elit, sed do eiusmod tempor incididunt ut labore et dolore magna aliqua.</p>
  <article class="price basic"><div class="name">Basic</div><div class="amt">$0</div><div class="term">14 Dyas</div><p>Lorem ipsum dolor sit amet, consectetur adipiscing elit, sed do eiusmod tempor incididunt ut labore et dolore magna</p><hr><a class="btn" style="background:var(--orange)">Learn More</a></article>
  <article class="price standard"><div class="name">Standard</div><div class="amt">$30</div><div class="term">1 Month</div><p>Lorem ipsum dolor sit amet, consectetur adipiscing elit, sed do eiusmod tempor incididunt ut labore et dolore magna</p><hr><a class="btn" style="background:#6fd6c2">Learn More</a></article>
  <article class="price pro"><div class="name">Pro</div><div class="amt">$150</div><div class="term">6 Month</div><p>Lorem ipsum dolor sit amet, consectetur adipiscing elit, sed do eiusmod tempor incididunt ut labore et dolore magna</p><hr><a class="btn" style="background:#22b3e2">Learn More</a></article>

  <!-- testimonials -->
  <h2 class="abs t-title">What Our Client's Sya<br>About Us</h2>
  <p class="abs t-text">Lorem ipsum dolor sit amet, consectetur adipiscing elit, sed do eiusmod tempor incididunt ut</p>
  <div class="abs t-figure" role="img" aria-label="Illustration of a standing man"></div>
  <div class="abs quote">
    <span class="mark">“</span>
    <p>Lorem ipsum dolor sit amet, consectetur adipiscing elit, sed do eiusmod tempor incididunt ut labore et dolore magna aliqua. Quis ipsum suspendisse ultrices gravida. Risus commodo viverra maecenas accumsan lacus vel facilisis.</p>
    <div class="who"><div class="avatar" style="width:16px;height:16px" role="img" aria-label="Client photo"></div><div><b>Mara Tellen</b><span>CEO at Quintrel</span></div></div>
    <svg class="abs" style="right:0;bottom:0" width="30" height="30" viewBox="0 0 30 30"><path d="M30 0V30H0C4 14 14 4 30 0Z" fill="#2e8fd0"/></svg>
  </div>
  <div class="orbit" style="left:372px;top:1488px;width:222px;height:222px"></div>
  <div class="orbit" style="left:425px;top:1541px;width:116px;height:116px"></div>
  <div class="abs avatar" style="left:420px;top:1526px;width:32px;height:32px" role="img" aria-label="Client photo"></div>
  <div class="abs avatar" style="left:517px;top:1560px;width:32px;height:32px" role="img" aria-label="Client photo"></div>
  <div class="abs avatar" style="left:362px;top:1587px;width:42px;height:42px" role="img" aria-label="Client photo"></div>
  <div class="abs avatar" style="left:467px;top:1583px;width:32px;height:32px" role="img" aria-label="Client photo"></div>
  <div class="abs avatar" style="left:420px;top:1661px;width:32px;height:32px" role="img" aria-label="Client photo"></div>
  <div class="abs avatar" style="left:502px;top:1648px;width:32px;height:32px" role="img" aria-label="Client photo"></div>

  <!-- partners -->
  <div class="abs partners"><span>Pictora</span><span>Frendly</span><span>Brisq</span><span>Zorvix</span><span>Yarvo</span></div>

  <!-- footer -->
  <footer class="abs footer">
    <div class="abs brand">KLT</div>
    <div class="fcol" style="left:134px;top:48px;line-height:1.6">
      <p>418 Harrow Lane, Fenwick,<br>Ohio, 40217</p>
      <p style="margin-top:6px">hello@velmorbix.com</p>
      <p style="margin-top:6px">+1 555 0142 88</p>
      <div class="social"><i></i><i></i><i class="pink"></i></div>
    </div>
    <div class="fcol" style="left:240px"><h5>Services</h5><p>Web Design</p><p>Web Development</p><p>Online Marketing</p><p>Seo</p><p>Wordpress</p><p>Content</p></div>
    <div class="fcol" style="left:328px"><h5>Company</h5><p>About</p><p>Services</p><p>Pricing</p><p>Term &amp; Condition</p><p>Privacy Policy</p><p>Contact</p></div>
    <div class="fcol news"><h5>Newsletter</h5><p style="line-height:1.6;margin-top:4px">Lorem ipsum dolor sit amet, consectetur adipiscing elit, sed do eiusmod temporenim</p><div class="news-input"><i></i></div></div>
    <div class="bottom"><span>© 2018 KLT. All Right Reserved</span><nav><span>Home</span><span>About</span><span>Services</span><span>Pricing</span><span>Testimonial</span><span>Blog</span><span>Contact</span></nav></div>
  </footer>

</main>
</body>
</html>
```